Scientific project description

Here is a project description related to cellular mechanics, showing above the forces acting on cells in the tissues of our body. The forces on single cells are there to depict how forces are acting on cells (pressure squeezes the cell, shear flow is pushing the upward parts of the cell, tension pulls one part of the cell, strain is stretching the whole cell; the single cell images are to be found also on the last page). Intense red/purple are used to indicate that the forces are stressful (the colors to be used do not need to be exactly like these colors). The picture in the middle is a view of cells (same picture on next page if that needs to be modified). At the left, a description of what happens when everything is going well, i.e. the body stays healthy. At the right, if you dysfunction you get disease. Green nuances were used to indicate health, brownish, perhaps not so pleasant nuances were used to indicate disease. Below are the steps of the project.

On the whole, we're rather happy with the concept description as such, but it should look a little bit nicer. To many color nuances give a "noisy" impression, fonts could be nicer, layout more crisp, and the text on the steps should be more readable. We would also like to have two versions of the same picture, one with black background, one with white.

Target Market(s)

Scientists that are evaluating our project

Requirements
Must have
• Easy to grasp the idea, easy to read and understand the underlying idea.
Nice to have
• Would be good to have the Concept title ("Vorlint Concept and Envisioned Project Progression) on top of the figure as indicated in the second brief picture submitted.

```html
<!DOCTYPE html>
<html lang="en">
<head>
<meta charset="utf-8">
<title>Vorlint Concept and Envisioned Project Progression</title>
<link rel="stylesheet" href="https://fonts.googleapis.com/css2?family=Montserrat:wght@500;600;700;800&display=swap">
<style>
  :root {
    --bg: #ffffff;
    --ink: #222222;
    --on-fill: #ffffff;
    --rule: #c8003f;
    --force-1: #e8102a;
    --force-2: #c8003f;
    --force-3: #b0003a;
    --force-4: #c0007e;
    --step: #c8003f;
    --fit-1: #5fc822;
    --fit-2: #4f9a22;
    --fit-3: #3a7a16;
    --frail-1: #f07a10;
    --frail-2: #d26a0c;
    --frail-3: #c94e0a;
    --cells-core: #b9e39a;
    --cells-mid: #8fcf5e;
    --cells-edge: rgba(143,207,94,0.25);
    --cells-out: rgba(143,207,94,0);
  }
  /* Dark edition of the same figure */
  .canvas--dark, .canvas.theme-dark {
    --bg: #0d0d0d;
    --ink: #f2f2f2;
    --rule: #e0245a;
  }
  @media (prefers-color-scheme: dark) {
    :root { --bg: #0d0d0d; --ink: #f2f2f2; --rule: #e0245a; }
  }

  * { margin: 0; padding: 0; box-sizing: border-box; }
  html, body { width: 1200px; height: 1200px; overflow: hidden; background: var(--bg); }
  body { font-family: "Montserrat", Arial, sans-serif; color: var(--ink); }
  .canvas { position: relative; width: 1200px; height: 1200px; background: var(--bg); color: var(--ink); }

  .title {
    position: absolute; left: 19px; top: 38px;
    font-size: 34.5px; font-weight: 800; letter-spacing: 0.3px; white-space: nowrap;
  }
  .title-rule { position: absolute; left: 51px; top: 106px; width: 1127px; height: 2px; background: var(--rule); border-radius: 1px; }

  .forces { position: absolute; left: 176px; top: 160px; width: 825px; height: 74px; display: flex; }
  .force {
    flex: 1; display: flex; align-items: center; justify-content: center;
    color: var(--on-fill); font-weight: 700; font-size: 27px; letter-spacing: 0.3px;
  }
  .force--pressure { background: var(--force-1); }
  .force--shear { background: var(--force-2); }
  .force--tension { background: var(--force-3); }
  .force--strain { background: var(--force-4); }
  .force-arrows { position: absolute; left: 0; top: 0; width: 1200px; height: 320px; pointer-events: none; }

  .cell-view {
    position: absolute; left: 412px; top: 398px; width: 352px; height: 236px;
    border-radius: 50%;
    background: radial-gradient(ellipse at center, var(--cells-core) 0%, var(--cells-mid) 45%, var(--cells-edge) 75%, var(--cells-out) 100%);
  }
  .mechanostasis {
    position: absolute; left: 440px; top: 493px; width: 296px; text-align: center;
    font-size: 25px; font-weight: 800; color: #1e1e1e;
  }

  .box {
    position: absolute; display: flex; align-items: center; justify-content: center;
    text-align: center; color: var(--on-fill); border-radius: 6px; line-height: 1.2;
  }
  .box--fitness { left: 114px; top: 479px; width: 186px; height: 57px; background: var(--fit-1); font-size: 23px; font-weight: 500; }
  .box--functional { left: 107px; top: 647px; width: 203px; height: 124px; background: var(--fit-2); font-size: 23px; font-weight: 500; }
  .box--health { left: 114px; top: 846px; width: 181px; height: 52px; background: var(--fit-3); font-size: 23px; font-weight: 500; }
  .box--frailty { left: 887px; top: 479px; width: 187px; height: 57px; background: var(--frail-1); font-size: 23px; font-weight: 700; padding-bottom: 12px; }
  .box--dysfunctional { left: 890px; top: 647px; width: 203px; height: 124px; background: var(--frail-2); font-size: 23px; font-weight: 700; padding-bottom: 6px; }
  .box--disease { left: 892px; top: 846px; width: 182px; height: 52px; background: var(--frail-3); font-size: 23px; font-weight: 700; }

  .flow-arrows { position: absolute; left: 0; top: 0; width: 1200px; height: 1200px; pointer-events: none; }

  .step {
    position: absolute; height: 41px; display: flex; align-items: center; justify-content: center;
    background: var(--step); color: var(--on-fill); font-size: 26.5px; font-weight: 700; white-space: nowrap;
  }
  .step--therapies { left: 490px; top: 705px; width: 195px; padding-bottom: 6px; }
  .step--prevention { left: 474px; top: 753px; width: 234px; }
  .step--targets { left: 464px; top: 801px; width: 253px; }
  .step--machineries { left: 435px; top: 849px; width: 311px; padding-bottom: 8px; }
  .step--responses { left: 374px; top: 895px; width: 428px; padding-bottom: 6px; }
  .step--disease-models { left: 352px; top: 943px; width: 472px; }
  .step--force-models { left: 328px; top: 999px; width: 519px; }
</style>
</head>
<body>
<main class="canvas">
  <h1 class="title">VORLINT CONCEPT AND ENVISIONED PROJECT PROGRESSION</h1>
  <div class="title-rule"></div>

  <div class="forces">
    <div class="force force--pressure">PRESSURE</div>
    <div class="force force--shear">SHEAR</div>
    <div class="force force--tension">TENSION</div>
    <div class="force force--strain">STRAIN</div>
  </div>

  <svg class="force-arrows" viewBox="0 0 1200 320" aria-hidden="true">
    <defs>
      <polygon id="force-arrow" points="-17,0 17,0 17,36 36,36 0,74 -36,36 -17,36"/>
    </defs>
    <use href="#force-arrow" fill="var(--force-1)" transform="translate(308 230) rotate(-28)"/>
    <use href="#force-arrow" fill="var(--force-2)" transform="translate(482 230) rotate(-14)"/>
    <use href="#force-arrow" fill="var(--force-3)" transform="translate(694 230) rotate(14)"/>
    <use href="#force-arrow" fill="var(--force-4)" transform="translate(870 230) rotate(26)"/>
  </svg>

  <div class="cell-view" role="img" aria-label="Cluster of round green cells around the mechanostasis label"></div>
  <div class="mechanostasis">MECHANOSTASIS</div>

  <div class="box box--fitness">Cell fitness</div>
  <div class="box box--functional">Functional<br>cellular<br>machineries</div>
  <div class="box box--health">Health</div>

  <div class="box box--frailty">Cell frailty</div>
  <div class="box box--dysfunctional">Dysfunctional<br>cellular<br>machineries</div>
  <div class="box box--disease">Disease</div>

  <svg class="flow-arrows" viewBox="0 0 1200 1200" aria-hidden="true">
    <defs>
      <polygon id="down-arrow" points="-6,0 6,0 6,18 15,18 0,36 -15,18 -6,18"/>
      <polygon id="side-arrow" points="0,-6 20,-6 20,-15 38,0 20,15 20,6 0,6"/>
    </defs>
    <use href="#side-arrow" fill="var(--fit-1)" transform="translate(378 506) scale(-1 1)"/>
    <use href="#side-arrow" fill="var(--frail-1)" transform="translate(798 506)"/>
    <use href="#down-arrow" fill="var(--fit-1)" transform="translate(202 574)"/>
    <use href="#down-arrow" fill="var(--fit-1)" transform="translate(202 794)"/>
    <use href="#down-arrow" fill="var(--frail-1)" transform="translate(989 574)"/>
    <use href="#down-arrow" fill="var(--frail-1)" transform="translate(989 794)"/>
  </svg>

  <div class="step step--therapies">Therapies</div>
  <div class="step step--prevention">Prevention</div>
  <div class="step step--targets">Critical targets</div>
  <div class="step step--machineries">Cellular machineries</div>
  <div class="step step--responses">Cell, tissue &amp; organ responses</div>
  <div class="step step--disease-models">Disease models</div>
  <div class="step step--force-models">Mechanical force models</div>
</main>
</body>
</html>
```